Branded Flyer Template Libraries Brightmoor Funding

Create one-page flyer templates for equipment finance industry to provide a fast turnaround that consistent on-brand for educational and promotional flyers that can be quickly customized with partners logos. These will become a standard toolkit for marketing for use in Adobe Illustrator and editable. customer facing are business owners considering equipment financing typically used for leave behind flyers, email, and handouts. vendor facing to equipment dealers, manufacturers and sales reps who refer customers to us, typically used at trade shows, co branded flyers, and email promotions.
Requesting 1-2 flyer templates with concepts for educational, and promotional.
Brand guide and current flyers in circulation are uploaded as reference.
Look and feel
Each slider illustrates characteristics of the customer's brand and the style your logo design should communicate.

```html
<!DOCTYPE html>
<html lang="en">
<head>
<meta charset="utf-8">
<title>Brightmoor Funding – How Equipment Financing Works</title>
<link rel="stylesheet" href="https://fonts.googleapis.com/css2?family=Merriweather:wght@400;700;900&family=Rubik:ital,wght@0,300;0,400;0,500;1,300&display=swap">
<style>
  :root {
    --green-deep: #0c4a2a;
    --green-brand: #0b6b3b;
    --green-light: #a9cd86;
    --card-bg: #eef5fa;
    --white: #ffffff;
    --sky-top: #9aa3a8;
    --sky-glow: #e8b66a;
    --ground: #4a3a26;
  }
  * { margin: 0; padding: 0; box-sizing: border-box; }
  html, body { width: 927px; height: 1200px; overflow: hidden; background: var(--white); }
  .flyer {
    position: relative; width: 927px; height: 1200px; overflow: hidden;
    background: var(--white); font-family: "Rubik", sans-serif; color: var(--green-deep);
  }
  .hero-photo {
    position: absolute; left: 0; top: 0; width: 927px; height: 700px;
    background: linear-gradient(180deg, #ffffff 0%, #d7d9d6 8%, var(--sky-top) 24%, #c9a98a 44%, var(--sky-glow) 58%, #8a6a3e 74%, var(--ground) 100%);
  }
  .hero-curves { position: absolute; left: 0; top: 0; width: 927px; height: 1200px; }
  .brand {
    position: absolute; top: 60px; left: 0; width: 927px;
    display: flex; justify-content: center; align-items: center; gap: 16px;
  }
  .brand-dot { width: 62px; height: 62px; border-radius: 50%; background: var(--green-brand); }
  .brand-block { display: flex; flex-direction: column; align-items: center; }
  .brand-name {
    font-family: "Merriweather", serif; font-weight: 900; font-size: 34px;
    color: var(--green-brand); letter-spacing: 0.5px; text-transform: uppercase;
  }
  .brand-tag {
    margin-top: 6px; font-size: 11px; font-weight: 500; letter-spacing: 4px;
    color: #1d1d1d; display: flex; align-items: center; gap: 8px;
  }
  .brand-tag::before, .brand-tag::after { content: ""; width: 26px; height: 1px; background: #1d1d1d; }
  .headline { position: absolute; top: 534px; left: 0; width: 927px; text-align: center; font-family: "Merriweather", serif; }
  .headline-kicker { font-size: 33px; font-weight: 400; color: var(--green-deep); line-height: 1.2; }
  .headline-main { font-size: 74px; font-weight: 900; color: var(--green-deep); line-height: 1.1; margin-top: 2px; }
  .intro {
    position: absolute; top: 676px; left: 0; width: 927px; text-align: center;
    font-size: 19px; line-height: 23px; color: var(--green-deep);
  }
  .section-pill {
    position: absolute; top: 752px; left: 321px; width: 284px; height: 43px;
    border-radius: 22px; background: var(--green-deep); color: var(--white);
    font-family: "Merriweather", serif; font-size: 26px;
    display: flex; align-items: center; justify-content: space-between; padding: 0 18px;
  }
  .section-pill span.dot { width: 7px; height: 7px; border-radius: 50%; background: var(--white); }
  .steps { position: absolute; top: 824px; left: 65px; display: flex; gap: 19px; }
  .step { background: var(--card-bg); height: 134px; padding-top: 16px; text-align: center; }
  .step:nth-child(1) { width: 249px; }
  .step:nth-child(2) { width: 262px; }
  .step:nth-child(3) { width: 249px; }
  .step-title {
    font-family: "Merriweather", serif; font-size: 21px; font-weight: 400; color: var(--green-deep);
    display: flex; align-items: center; justify-content: center; gap: 8px; white-space: nowrap;
  }
  .step-marker {
    width: 22px; height: 22px; border-radius: 50%; border: 2px solid var(--green-light);
    display: flex; align-items: center; justify-content: center; flex-shrink: 0;
  }
  .step-marker::after { content: ""; width: 11px; height: 11px; border-radius: 50%; background: var(--green-deep); }
  .step-text { margin-top: 10px; font-size: 17.5px; font-weight: 300; line-height: 22px; color: var(--green-deep); }
  .cta-question {
    position: absolute; top: 984px; left: 0; width: 927px; text-align: center;
    font-size: 28px; font-style: italic; font-weight: 300; color: var(--green-deep);
  }
  .cta-heading {
    position: absolute; top: 1024px; left: 0; width: 927px; text-align: center;
    font-family: "Merriweather", serif; font-size: 37px; font-weight: 900; color: var(--green-deep);
  }
  .treeline {
    position: absolute; top: 1086px; left: 0; width: 927px; height: 64px;
    background: linear-gradient(180deg, rgba(12,74,42,0) 0%, rgba(12,74,42,0.55) 45%, var(--green-deep) 100%);
  }
  .contact-bar {
    position: absolute; top: 1148px; left: 0; width: 927px; height: 52px;
    background: var(--green-deep); color: var(--white);
    display: flex; align-items: center; justify-content: center; gap: 16px;
    font-size: 19px; font-weight: 500;
  }
  .contact-bar .divider { font-weight: 400; }
</style>
</head>
<body>
<main class="flyer">
  <div class="hero-photo" role="img" aria-label="Photo of a site worker in hard hat and safety vest watching an excavator load a dump truck beside a wheel loader at sunset"></div>

  <svg class="hero-curves" viewBox="0 0 927 1200" aria-hidden="true">
    <path d="M0,523 C150,470 300,436 465,436 C650,436 800,470 927,505 L927,1200 L0,1200 Z" fill="var(--green-light)"/>
    <path d="M618,457 C750,462 860,485 927,509 L927,567 C840,520 730,470 618,457 Z" fill="var(--green-deep)"/>
    <path d="M0,603 C160,530 330,482 490,482 C330,500 150,580 0,700 Z" fill="var(--green-deep)"/>
    <path d="M0,676 C150,560 320,488 490,486 C690,486 830,560 927,618 L927,1200 L0,1200 Z" fill="var(--white)"/>
  </svg>

  <header class="brand">
    <div class="brand-dot"></div>
    <div class="brand-block">
      <div class="brand-name">Brightmoor Funding</div>
      <div class="brand-tag">EQUIPMENT FINANCE</div>
    </div>
  </header>

  <section class="headline">
    <div class="headline-kicker">How Equipment</div>
    <div class="headline-main">Financing Works</div>
  </section>

  <p class="intro">Equipment financing helps businesses acquire essential equipment<br>while preserving cash flow and maintaining financial flexibility.</p>

  <div class="section-pill"><span class="dot"></span>How It Works<span class="dot"></span></div>

  <section class="steps">
    <article class="step">
      <h3 class="step-title"><span class="step-marker"></span>Choose Equipment</h3>
      <p class="step-text">Select the equipment<br>your business needs.</p>
    </article>
    <article class="step">
      <h3 class="step-title"><span class="step-marker"></span>Apply For Financing</h3>
      <p class="step-text">Complete a simple<br>application process.</p>
    </article>
    <article class="step">
      <h3 class="step-title"><span class="step-marker"></span>Receive Funding</h3>
      <p class="step-text">Get approved and<br>put your equipment<br>to work.</p>
    </article>
  </section>

  <p class="cta-question">Have Questions About Equipment Financing?</p>
  <h2 class="cta-heading">Let’s Discuss Your Financing Options</h2>

  <div class="treeline" role="img" aria-label="Silhouette of an evergreen forest treeline"></div>

  <footer class="contact-bar">
    <span>brightmoorfunding.com</span><span class="divider">|</span>
    <span>hello@brightmoorfunding.com</span><span class="divider">|</span>
    <span>(800) 555-0148</span>
  </footer>
</main>
</body>
</html>
```